Website design for Nutraceutical Contract Manufacturer in NJ

Develop website for a contract manufacturer, specializing in nutraceutical products. Our color theme is based on the colors of the American flag (Pantone blue no. 282 & red no. 193, white), representing a US presence of a company based in Italy. Our website will include a general e-mail box link for additional info. requests, color photos of our operation, a link to our parent company's website, a video, a mission statement, a description of our capabilities.Our internet presence will be on a B2B basis, to include a map of our location and contact information.

Target Market(s)

Businesses seeking contract manufacturer in the US nutraceutical industry.

Industry/Entity Type

Manufacturer

Number of Pages Required

3 page

Font styles to use
Sans Serif

Colors
3176b5
f04a50

Requirements
Must have
• Colors, as described in project description section. Three pages minimum - one to define what we do/location/contact info,/links to affiliated companies, one to showcase certifications, one to provide photos. We are open to having additional pages as suggested, if necessary. Our website for contacts info: www.kelvoranto-us.com .
• Link to our general email box: info@kelvoranto-us.com
• Pantone colors detailed in project description.
• HTTPS secure presence
Nice to have
• TBD
Should not have
• PROFANITY

```html
<!DOCTYPE html>
<html lang="en">
<head>
<meta charset="utf-8">
<title>Kelvoranto US – Contract Manufacturing</title>
<link href="https://fonts.googleapis.com/css2?family=Lato:wght@400;700;900&display=swap" rel="stylesheet">
<style>
:root{
  --blue:#3176b5;
  --blue-deep:#22508f;
  --navy:#1c2c63;
  --red:#f04a50;
  --red-deep:#c8283a;
  --ink:#2b2f3a;
  --muted:#6c7180;
  --white:#ffffff;
  --line:#e3e6ee;
}
*{box-sizing:border-box;margin:0;padding:0}
html,body{width:1200px;height:2632px;overflow:hidden;background:var(--white)}
body{font-family:'Lato',sans-serif;color:var(--ink);position:relative}
a{color:inherit;text-decoration:none}

/* header */
.site-header{position:absolute;top:0;left:0;width:1200px;height:96px;background:var(--white);border-bottom:3px solid var(--red);z-index:5}
.brand{position:absolute;left:40px;top:22px;font-size:42px;font-weight:700;color:var(--red);letter-spacing:.5px;display:flex;align-items:center;gap:12px}
.brand-dot{width:16px;height:16px;background:var(--blue);border-radius:50%}
.topbar{position:absolute;right:40px;top:8px;display:flex;align-items:center;gap:22px;font-size:13px;color:var(--muted)}
.topbar span{display:flex;align-items:center;gap:6px}
.socials{display:flex;gap:6px}
.socials i{display:block;width:22px;height:22px;background:var(--red)}
.main-nav{position:absolute;right:40px;top:58px;display:flex;gap:40px;font-size:15px;color:var(--ink)}
.main-nav a.active{color:var(--red)}

/* hero */
.hero{position:absolute;top:96px;left:0;width:1200px;height:500px;overflow:hidden}
.hero-photo{position:absolute;inset:0;background:linear-gradient(120deg,#9ba6b8 0%,#dfe4ec 35%,#5c6f91 70%,#2e4a7a 100%)}
.hero-tint{position:absolute;inset:0;background:linear-gradient(90deg,rgba(34,80,143,.45),rgba(34,80,143,.75))}
.hero-content{position:absolute;left:0;right:0;top:70px;text-align:center;color:var(--white)}
.hero h1{font-size:58px;font-weight:900;letter-spacing:1px;margin-left:260px}
.hero p{width:520px;margin:16px 0 0 460px;font-size:15px;line-height:1.5;text-align:center}
.btn{display:inline-block;background:var(--red);color:var(--white);font-size:15px;font-weight:700;padding:14px 26px;border-radius:3px;letter-spacing:.5px}
.hero .btn{margin:26px 0 0 260px}
.hero-wave{position:absolute;left:0;bottom:-1px;width:1200px;height:110px}

/* about */
.about{position:absolute;top:600px;left:0;width:1200px;height:540px}
.section-title{font-size:36px;font-weight:900;color:var(--blue-deep)}
.section-title em{font-style:normal;color:var(--red)}
.about .section-title{position:absolute;left:80px;top:190px}
.about-lead{position:absolute;left:80px;top:250px;width:560px;font-size:19px;line-height:1.5;color:var(--blue)}
.about-list{position:absolute;left:80px;top:340px;list-style:none;width:560px}
.about-list li{display:flex;align-items:center;gap:18px;font-size:14px;color:var(--muted);margin-bottom:18px}
.about-list li::before{content:"";width:14px;height:14px;background:var(--navy);transform:rotate(45deg);flex:none}
.video{position:absolute;left:690px;top:180px;width:430px;height:230px;background:linear-gradient(135deg,#c64a55,#e8868c 50%,#9b2d3c);box-shadow:-18px 18px 0 var(--blue-deep)}
.video svg{position:absolute;left:185px;top:85px}

/* mission */
.mission{position:absolute;top:1140px;left:0;width:1200px;height:560px;overflow:hidden}
.mission-photo{position:absolute;inset:0;background:linear-gradient(90deg,#b9c4d3,#eef1f5 40%,#d2dae6 70%,#9aa9c0)}
.mission-tint{position:absolute;inset:0;background:rgba(49,118,181,.35)}
.mission-card{position:absolute;left:330px;top:20px;width:540px;height:520px;background:rgba(34,80,143,.82);text-align:center;color:var(--white);padding:30px 40px}
.mission-card h2{font-size:32px;font-weight:700;display:inline-block;border-bottom:3px solid var(--red);padding-bottom:6px}
.mission-card p{font-size:15px;line-height:1.6;margin:22px 0 26px}

/* what we do */
.services{position:absolute;top:1700px;left:0;width:1200px;height:460px}
.services-photo{position:absolute;left:80px;top:30px;width:440px;height:290px;background:linear-gradient(135deg,#dfe3e8,#b7bec8 50%,#8b95a3)}
.services .section-title{position:absolute;left:560px;top:30px}
.services p{position:absolute;left:560px;top:90px;width:560px;font-size:14px;line-height:1.65;color:var(--muted)}
.services .btn{position:absolute;left:560px;top:258px}

/* footer */
.site-footer{position:absolute;top:2140px;left:0;width:1200px;height:492px;background:var(--navy);color:var(--white);overflow:hidden}
.footer-shape{position:absolute;left:0;top:0;width:1200px;height:492px}
.footer-brand{position:absolute;left:70px;top:150px;font-size:38px;font-weight:700;color:var(--white)}
.team{position:absolute;left:80px;top:215px;list-style:none}
.team li{margin-bottom:12px;font-size:12px;line-height:1.4}
.team strong{display:block;font-size:16px;font-weight:700}
.footer-col{position:absolute;top:150px}
.footer-col h3{font-size:22px;font-weight:700;margin-bottom:22px}
.contact-col{left:580px}
.contact-col li{display:flex;gap:14px;font-size:12px;margin-bottom:16px;line-height:1.4;list-style:none}
.links-col{left:920px}
.links-col li{list-style:none;font-size:13px;margin-bottom:12px}
.newsletter{position:absolute;left:580px;top:395px;width:560px;height:46px;background:var(--white);border-radius:23px;color:var(--muted);font-size:13px;padding:15px 24px}
.newsletter b{position:absolute;right:4px;top:4px;width:38px;height:38px;border-radius:50%;background:var(--red)}
.copyright{position:absolute;left:580px;top:462px;width:560px;text-align:center;font-size:12px;color:#c7cde0}
</style>
</head>
<body>

<header class="site-header">
  <a class="brand" href="#">Kelvoranto US <span class="brand-dot"></span></a>
  <div class="topbar">
    <span><svg width="12" height="14" viewBox="0 0 12 14"><path d="M6 0a5 5 0 0 0-5 5c0 4 5 9 5 9s5-5 5-9a5 5 0 0 0-5-5zm0 7a2 2 0 1 1 0-4 2 2 0 0 1 0 4z" fill="#f04a50"/></svg>18 Orchard Way Millbrook, NJ 08999 USA</span>
    <span><svg width="13" height="13" viewBox="0 0 24 24"><path d="M6.6 10.8a15 15 0 0 0 6.6 6.6l2.2-2.2a1 1 0 0 1 1-.2 11 11 0 0 0 3.6.6 1 1 0 0 1 1 1V20a1 1 0 0 1-1 1A17 17 0 0 1 3 4a1 1 0 0 1 1-1h3.5a1 1 0 0 1 1 1 11 11 0 0 0 .6 3.6 1 1 0 0 1-.3 1z" fill="#f04a50"/></svg>+1 (555) 0142-7788</span>
    <div class="socials"><i></i><i></i><i></i></div>
  </div>
  <nav class="main-nav">
    <a class="active" href="#">Home</a><a href="#">About Us</a><a href="#">Our Mission</a><a href="#">What We Do</a><a href="#">Contact Us</a>
    <svg width="16" height="16" viewBox="0 0 16 16"><circle cx="7" cy="7" r="5" fill="none" stroke="#6c7180" stroke-width="2"/><path d="M11 11l4 4" stroke="#6c7180" stroke-width="2"/></svg>
  </nav>
</header>

<section class="hero">
  <div class="hero-photo" role="img" aria-label="Snowy exterior of the company building with its entrance sign"></div>
  <div class="hero-tint"></div>
  <div class="hero-content">
    <h1>Kelvoranto US LLC</h1>
    <p>Quality supplements made to order in New Jersey. We help brands bring reliable products to market with careful sourcing, clean production lines and a team that keeps every batch on schedule and on spec.</p>
    <a class="btn" href="#">LEARN MORE</a>
  </div>
  <svg class="hero-wave" viewBox="0 0 1200 110" preserveAspectRatio="none">
    <path d="M0 40 C300 120 700 110 1200 20 L1200 110 L0 110 Z" fill="#ffffff"/>
  </svg>
</section>

<section class="about">
  <h2 class="section-title">About <em>Kelvoranto US</em></h2>
  <p class="about-lead">Kelvoranto US LLC is a contract manufacturer for the food supplements market, producing exclusively for third parties.</p>
  <ul class="about-list">
    <li>Full production runs built around each partner's formula.</li>
    <li>Certified facility with strict quality checks at every stage.</li>
    <li>Flexible batch sizes for new and growing supplement brands.</li>
  </ul>
  <div class="video" role="img" aria-label="Video still of the clean room production area">
    <svg width="60" height="60" viewBox="0 0 60 60"><circle cx="30" cy="30" r="30" fill="#ffffff"/><path d="M24 18 L42 30 L24 42 Z" fill="#f04a50"/></svg>
  </div>
</section>

<section class="mission">
  <div class="mission-photo" role="img" aria-label="Bright production corridor with stainless steel equipment"></div>
  <div class="mission-tint"></div>
  <div class="mission-card">
    <h2>Our Mission</h2>
    <p>The mission of Kelvoranto US is to be the premier contract manufacturer of dietary supplements in the United States, offering quality and excellence to our customers. Being a premier company does not mean being the biggest, but it does mean being the best in terms of customer service, employee talent and consistent growth. All employees are committed to this vision and are always striving to exceed all standards of the industry.</p>
    <a class="btn" href="#">LEARN MORE</a>
  </div>
</section>

<section class="services">
  <div class="services-photo" role="img" aria-label="Laboratory scale and testing instruments on a bench"></div>
  <h2 class="section-title">What <em>We DO?</em></h2>
  <p>From powders and capsules to tablets and liquid blends, our team handles formulation support, raw material sourcing, blending, encapsulation and packaging under one roof. Each project is guided by a dedicated manager who keeps partners informed from first sample to final shipment. Our lab tests every lot for identity, purity and strength, so brands can launch with confidence and reorder with ease as their demand grows.</p>
  <a class="btn" href="#">LEARN MORE</a>
</section>

<footer class="site-footer">
  <svg class="footer-shape" viewBox="0 0 1200 492" preserveAspectRatio="none">
    <path d="M0 0 H1200 V40 C900 20 700 30 520 110 V492 H0 Z" fill="#c8283a"/>
    <path d="M0 0 H1200 V20 C800 0 500 20 0 110 Z" fill="#ffffff"/>
  </svg>
  <div class="footer-brand">Kelvoranto US</div>
  <ul class="team">
    <li><strong>Marco Venturi</strong>President : marco.venturi@kelvoranto-us.com</li>
    <li><strong>Peter Hollis</strong>Member : peter.hollis@kelvoranto-us.com</li>
    <li><strong>Paolo Renzi</strong>Quality Assurance : paolo.renzi@kelvoranto-us.com</li>
    <li><strong>Linda Carrow</strong>Business Manager : linda.carrow@kelvoranto-us.com</li>
  </ul>
  <div class="footer-col contact-col">
    <h3>Contact Us</h3>
    <ul>
      <li><svg width="12" height="14" viewBox="0 0 12 14"><path d="M6 0a5 5 0 0 0-5 5c0 4 5 9 5 9s5-5 5-9a5 5 0 0 0-5-5zm0 7a2 2 0 1 1 0-4 2 2 0 0 1 0 4z" fill="#fff"/></svg><span>18 Orchard Way Millbrook,<br>NJ 08999 USA</span></li>
      <li><svg width="13" height="13" viewBox="0 0 24 24"><path d="M6.6 10.8a15 15 0 0 0 6.6 6.6l2.2-2.2a1 1 0 0 1 1-.2 11 11 0 0 0 3.6.6 1 1 0 0 1 1 1V20a1 1 0 0 1-1 1A17 17 0 0 1 3 4a1 1 0 0 1 1-1h3.5a1 1 0 0 1 1 1 11 11 0 0 0 .6 3.6 1 1 0 0 1-.3 1z" fill="#fff"/></svg>+1 (555) 0142-7788</li>
      <li><svg width="13" height="13" viewBox="0 0 24 24"><path d="M6.6 10.8a15 15 0 0 0 6.6 6.6l2.2-2.2a1 1 0 0 1 1-.2 11 11 0 0 0 3.6.6 1 1 0 0 1 1 1V20a1 1 0 0 1-1 1A17 17 0 0 1 3 4a1 1 0 0 1 1-1h3.5a1 1 0 0 1 1 1 11 11 0 0 0 .6 3.6 1 1 0 0 1-.3 1z" fill="#fff"/></svg>+1 (555) 0163-2290</li>
      <li><svg width="14" height="11" viewBox="0 0 14 11"><rect x=".5" y=".5" width="13" height="10" fill="none" stroke="#fff"/><path d="M.5.5 7 6l6.5-5.5" fill="none" stroke="#fff"/></svg>info@kelvoranto-us.com</li>
    </ul>
  </div>
  <div class="footer-col links-col">
    <h3>Quick Links</h3>
    <ul><li>Home</li><li>About</li><li>Our Mission</li><li>What we do?</li><li>Contact Us</li></ul>
  </div>
  <div class="newsletter">Enter Email<b></b></div>
  <p class="copyright">Copyright © 2018, KELVORANTO US . All rights reserved. Privacy Policy.</p>
</footer>

</body>
</html>
```